Modern Homepage Design for brenvik.nl – Fish & Chicken Food Webshop

Brenvik.nl is an online store that sells fish and chicken food. The design should be visually appealing, easy to navigate, and optimized for e-commerce. We want a layout that helps customers quickly find what they need and encourages them to explore our products.
A good example of the style and structure we like is dierkamp.nl – clean layout, clear product focus, and user-friendly navigation.
Brand Colors (must be used):
Orange: #f7a441
Dark Gray: #3c3c3b
White: #ffffff
Please use these colors consistently throughout the design.
Homepage Requirements:
The homepage should include the following sections:
Main Slider / Hero Banner
A large, eye-catching slider at the top of the page to highlight promotions or featured categories.
Category Blocks
A section with clear, clickable blocks or tiles that link to main product categories (e.g., Fish Food, Chicken Food, Accessories).
Featured Products
A section showcasing selected or best-selling products.
Special Offers / Promotions
A space to highlight current deals or limited-time offers.
Three Banners in a Row
A section with three horizontal banners side by side, which can be used for promotions, shipping info, or other key messages.
Unique Selling Points (USPs)
A section that briefly explains what makes our store different (e.g., fast delivery, high-quality feed, trusted by professionals).
SEO Content Block
A short paragraph of text for SEO purposes (use Lorem Ipsum for dummy content).
Footer Design
Include space for contact information, navigation links, and social media.
Design Notes:
The design must be responsive and mobile-friendly.
Focus on clean layout, good spacing, and easy navigation.
Use modern fonts and a clear visual hierarchy.
We are only looking for the homepage design at this stage, but we may work with the selected designer on additional pages later.
Deliverables:
Homepage design in layered PSD, Figma, or Adobe XD format
Any fonts and assets used
Preview images/mockups
We look forward to seeing your ideas and working with a designer who can bring our brand to life with a fresh and functional homepage design.
Let us know if you have any questions.
Hobby Animal Keepers, Pet Owners
Animal Nutrition & Feed
2 page

```html
<!DOCTYPE html>
<html lang="en">
<head>
<meta charset="utf-8">
<title>Brenvik – Fish &amp; Chicken Food Webshop</title>
<link href="https://fonts.googleapis.com/css2?family=Outfit:wght@300;400;500;600;700&display=swap" rel="stylesheet">
<style>
:root{
  --orange:#f7a441;
  --dark:#3c3c3b;
  --white:#ffffff;
  --cream:#fbf1e4;
  --ink:#1f1f1f;
  --muted:#5a5a5a;
  --footer:#2f2f2e;
}
*{box-sizing:border-box;margin:0;padding:0}
html,body{width:1200px;height:2828px;overflow:hidden;background:var(--white)}
body{font-family:'Outfit',sans-serif;color:var(--ink);position:relative}
.abs{position:absolute}
a{color:inherit;text-decoration:none}

.topbar{left:0;top:0;width:1200px;height:27px;background:var(--orange);color:var(--white);font-size:12.5px;font-weight:500}
.topbar .ship{left:134px;top:6px}
.topbar .contact{left:888px;top:6px}
.topbar .sep{left:967px;top:0;width:1px;height:27px;background:rgba(255,255,255,.6)}
.topbar .account{left:983px;top:6px;display:flex;gap:6px;align-items:center}

.wordmark{font-weight:700;line-height:1;white-space:nowrap}
.header-logo{left:132px;top:48px;font-size:40px;color:var(--dark)}
.search{left:349px;top:53px;width:426px;height:35px;border:1px solid var(--dark);border-radius:18px;font-size:11px;color:var(--muted);padding:11px 17px}
.search svg{position:absolute;right:14px;top:9px}
.cart-btn{left:923px;top:53px;width:147px;height:35px;border-radius:18px;background:var(--orange);color:var(--white);font-weight:600;font-size:14px;display:flex;align-items:center;justify-content:center;gap:8px}

.mainnav{left:0;top:114px;width:1200px;height:35px;background:var(--dark)}
.mainnav ul{list-style:none;display:flex;justify-content:space-between;width:938px;margin-left:133px;padding-top:11px;font-size:10.5px;font-weight:500;color:var(--white)}
.mainnav li.active{color:var(--orange)}

.hero-main{left:131px;top:172px;width:622px;height:258px;border-radius:14px;background:#9fd3e5;overflow:hidden}
.hero-main .photo-left{left:0;top:30px;width:240px;height:228px;background:linear-gradient(160deg,#d9b98f,#c88a5a)}
.hero-main .photo-right{left:420px;top:20px;width:202px;height:238px;background:linear-gradient(160deg,#f1ece3,#c79a6c)}
.hero-main h1{left:243px;top:40px;font-size:31px;font-weight:700;letter-spacing:.5px}
.hero-main p{left:245px;top:84px;width:170px;font-size:11.5px;line-height:1.35}
.btn{background:var(--orange);color:var(--white);border-radius:16px;font-weight:600;display:flex;align-items:center;justify-content:center}
.hero-main .btn{left:247px;top:146px;width:97px;height:29px;font-size:13px}
.hero-side{left:765px;top:173px;width:305px;height:258px;border-radius:14px;background:linear-gradient(135deg,#f2c4c6,#e8a8ad)}
.hero-side h2{left:26px;top:18px;font-size:16px;font-weight:700;line-height:1.25}
.hero-side .btn{left:26px;top:68px;width:98px;height:28px;font-size:13px}
.hero-side .photo{left:50px;top:95px;width:200px;height:150px;border-radius:10px;background:linear-gradient(150deg,#9cc7a6,#e0c39a)}
.dots{left:403px;top:446px;display:flex;gap:8px}
.dots span{width:9px;height:9px;border-radius:50%;border:1px solid var(--dark)}
.dots span.on{background:var(--orange);border-color:var(--orange)}

.section-title{left:130px;font-size:17px;font-weight:700;letter-spacing:.3px}

.categories{left:131px;top:561px;width:939px;display:flex;gap:7px}
.cat{width:128px;text-align:center;font-size:12px}
.cat .tile{height:98px;border-radius:10px;margin-bottom:15px}

.product{top:782px;width:120px;font-size:11.5px}
.product .pack{width:90px;height:129px;border-radius:6px;margin-left:6px}
.stars{margin-top:24px;color:#f5b400;font-size:11px;letter-spacing:1px}
.product .name{margin-top:5px;line-height:1.3;font-weight:500}
.product .price{margin-top:10px;font-weight:600;font-size:12.5px}
.product .price s{font-weight:400;font-size:8.5px;color:var(--muted);margin-left:4px;text-decoration:none}
.arrow{width:25px;height:25px;border-radius:50%;background:var(--orange);display:flex;align-items:center;justify-content:center}

.offer{top:1098px;width:303px;height:249px;border-radius:12px;background:var(--cream);overflow:hidden}
.offer .kicker{font-size:16.5px;font-weight:700;color:var(--orange);text-align:center}
.offer .head{font-size:16px;font-weight:700;text-align:center}
.offer .txt{font-size:10px;line-height:1.45;text-align:center;color:var(--muted);margin-top:8px}
.offer .btn{width:85px;height:25px;font-size:11px;margin:12px auto 0}
.offer .photo{position:absolute;border-radius:8px}

.trust{left:132px;top:1411px;width:935px;height:71px;border-radius:36px;background:var(--cream);display:flex}
.trust .item{flex:1;display:flex;align-items:center;justify-content:center;gap:18px;font-size:13px;line-height:1.35;border-right:2px solid var(--white)}
.trust .item:last-child{border-right:0}

.usp{top:1552px;text-align:center}
.usp svg{display:block;margin:0 auto;height:44px}
.usp h3{font-size:16px;font-weight:600;margin-top:21px}
.usp p{font-size:10px;color:var(--muted);line-height:1.45;margin-top:7px}
.usp-sep{top:1537px;width:1px;height:154px;background:#d8c9b5}

.blog{top:1788px;width:224px;height:326px;border:1px solid #8d8d8d;border-radius:10px;overflow:hidden}
.blog .photo{height:155px}
.blog h4{font-size:13px;font-weight:500;line-height:1.35;margin:22px 18px 0 20px}
.blog p{font-size:10px;line-height:1.3;color:var(--muted);margin:8px 18px 0 20px}
.blog .btn{width:78px;height:23px;font-size:10.5px;margin:14px 0 0 22px}

.faq{left:130px;top:2186px;width:938px;list-style:none}
.faq li{height:37.4px;border-bottom:1px solid #9a9a9a;display:flex;justify-content:space-between;align-items:center;padding:0 12px 0 20px;font-size:13px}
.faq li:last-child{border-bottom:0}

.footer{left:0;top:2532px;width:1200px;height:296px;background:var(--footer);color:var(--white)}
.footer-logo{left:132px;top:86px;font-size:50px;color:var(--white)}
.footer h5{font-size:11px;font-weight:700;letter-spacing:.3px}
.footer .col{top:45px;font-size:10px;line-height:1.45}
.footer .contact-row{display:flex;gap:12px;align-items:flex-start;margin-top:12px}
.footer .menu{display:grid;grid-template-columns:70px 90px;margin-top:8px}
.footer .email{margin-top:12px;width:238px;height:28px;border-radius:14px;background:var(--white);color:var(--ink);display:flex;align-items:center;gap:12px;padding-left:14px;font-size:10px}
.footer .subscribe{margin-top:6px;width:238px;height:28px;border-radius:14px;background:var(--orange);font-size:13px;font-weight:600;display:flex;align-items:center;justify-content:center}
.footer .rule{left:130px;top:203px;width:937px;height:1px;background:#555}
.footer .follow{left:134px;top:237px;display:flex;align-items:center;gap:16px;font-size:10px;font-weight:700}
.footer .social{display:flex;gap:5px}
.footer .social span{width:20px;height:20px;border-radius:50%;background:var(--white)}
.footer .copy{right:134px;top:240px;font-size:10.5px}
</style>
</head>
<body>

<div class="abs topbar">
  <span class="abs ship">Free shipping from €29</span>
  <span class="abs contact">Contact us</span>
  <span class="abs sep"></span>
  <span class="abs account"><svg width="12" height="12" viewBox="0 0 12 12" fill="none" stroke="#fff" stroke-width="1.2"><circle cx="6" cy="3.5" r="2.5"/><path d="M1 11.5c0-3 2.2-4.5 5-4.5s5 1.5 5 4.5"/></svg>My Account</span>
</div>

<header>
  <a class="abs wordmark header-logo">Brenvik</a>
  <div class="abs search">Searching for
    <svg width="16" height="16" viewBox="0 0 16 16" fill="none" stroke="#1f1f1f" stroke-width="1.4"><circle cx="7" cy="7" r="5"/><path d="M11 11l4 4"/></svg>
  </div>
  <a class="abs cart-btn"><svg width="20" height="18" viewBox="0 0 20 18" fill="none" stroke="#fff" stroke-width="1.5"><path d="M1 1h3l2 10h11l2-7H5"/><circle cx="8" cy="15" r="1.5"/><circle cx="16" cy="15" r="1.5"/></svg>Shopping Cart</a>
</header>

<nav class="abs mainnav">
  <ul>
    <li class="active">FISHING</li><li>BIRDS</li><li>DOGS</li><li>CHICKENS</li><li>RODENT</li><li>ANGLING</li><li>REPTILES</li><li>FARM ANIMALS</li><li>OTHER PRODUCTS</li><li>GARDEN ANIMALS</li>
  </ul>
</nav>

<section class="abs hero-main">
  <div class="abs photo-left" role="img" aria-label="Dog food bags, rope toy and kibble"></div>
  <div class="abs photo-right" role="img" aria-label="Happy terrier dog with collar"></div>
  <h1 class="abs">PET FOOD</h1>
  <p class="abs">Lorem ipsum dolor sit amet, consectetur adipiscing elit, sed do eiusmod tempo.</p>
  <a class="abs btn">Shop Now</a>
</section>
<section class="abs hero-side">
  <h2 class="abs">PREMIUM FISH FEED<br>FOR EVERY TANK</h2>
  <a class="abs btn">Shop Now</a>
  <div class="abs photo" role="img" aria-label="Pet food pouches with a bowl of kibble"></div>
</section>
<div class="abs dots"><span class="on"></span><span></span><span></span><span></span><span></span></div>

<h2 class="abs section-title" style="top:504px">CATEGORIES</h2>
<div class="abs categories">
  <div class="cat"><div class="tile" style="background:#a9d2e3" role="img" aria-label="Carp fish"></div>Fishing</div>
  <div class="cat"><div class="tile" style="background:#f5d9d9" role="img" aria-label="Hummingbird"></div>Birds</div>
  <div class="cat"><div class="tile" style="background:#cfe8d2" role="img" aria-label="Border collie dog"></div>Dogs</div>
  <div class="cat"><div class="tile" style="background:#d9d4ce" role="img" aria-label="Brown hen"></div>Chickens</div>
  <div class="cat"><div class="tile" style="background:#fbe8d8" role="img" aria-label="Hamster"></div>Rodent</div>
  <div class="cat"><div class="tile" style="background:#ccf3ee" role="img" aria-label="Turtle"></div>Reptiles</div>
  <div class="cat"><div class="tile" style="background:#f3f0de" role="img" aria-label="White goat"></div>Farm animals</div>
</div>

<h2 class="abs section-title" style="top:733px">FEATURED PRODUCTS</h2>
<div class="abs arrow" style="left:82px;top:834px"><svg width="10" height="10" viewBox="0 0 10 10" fill="none" stroke="#fff" stroke-width="1.8"><path d="M6.5 1.5L3 5l3.5 3.5"/></svg></div>
<div class="abs arrow" style="left:1079px;top:834px"><svg width="10" height="10" viewBox="0 0 10 10" fill="none" stroke="#fff" stroke-width="1.8"><path d="M3.5 1.5L7 5 3.5 8.5"/></svg></div>
<div class="abs product" style="left:130px"><div class="pack" style="background:linear-gradient(160deg,#d98a2c,#5a3418)" role="img" aria-label="Dog food bag"></div><div class="stars">★★★★★</div><div class="name">Lorem ipsum dolor<br>sit amet that.</div><div class="price">€2.29<s>€6.29</s></div></div>
<div class="abs product" style="left:256px"><div class="pack" style="background:linear-gradient(160deg,#e6cfae,#b88a5c)" role="img" aria-label="Kraft food pouch"></div><div class="stars">★★★★★</div><div class="name">Lorem ipsum dolor<br>sit amet that.</div><div class="price">€2.29<s>€6.29</s></div></div>
<div class="abs product" style="left:388px"><div class="pack" style="background:linear-gradient(160deg,#d8c4a6,#a7c59a)" role="img" aria-label="Dog food bags"></div><div class="stars">★★★★★</div><div class="name">Lorem ipsum dolor<br>sit amet that.</div><div class="price">€2.29<s>€6.29</s></div></div>
<div class="abs product" style="left:530px"><div class="pack" style="background:linear-gradient(160deg,#f5c21a,#d6631c)" role="img" aria-label="Yellow dog food bag"></div><div class="stars">★★★★★</div><div class="name">Lorem ipsum dolor<br>sit amet that.</div><div class="price">€2.29<s>€6.29</s></div></div>
<div class="abs product" style="left:672px"><div class="pack" style="background:linear-gradient(180deg,#e9b23c,#4a9cc7 55%,#7a5a3a)" role="img" aria-label="Open pet food tin"></div><div class="stars">★★★★★</div><div class="name">Lorem ipsum dolor<br>sit amet that.</div><div class="price">€2.29<s>€6.29</s></div></div>
<div class="abs product" style="left:821px"><div class="pack" style="background:linear-gradient(160deg,#2f6ea3,#c9a45a)" role="img" aria-label="Blue kibble bag"></div><div class="stars">★★★★★</div><div class="name">Lorem ipsum dolor<br>sit amet that.</div><div class="price">€2.29<s>€6.29</s></div></div>
<div class="abs product" style="left:967px"><div class="pack" style="background:linear-gradient(160deg,#9dbb3a,#4f6a22)" role="img" aria-label="Green dog food bag"></div><div class="stars">★★★★★</div><div class="name">Lorem ipsum dolor<br>sit amet that.</div><div class="price">€2.29<s>€6.29</s></div></div>

<h2 class="abs section-title" style="top:1056px">SPECIAL OFFERS</h2>
<div class="abs offer" style="left:131px">
  <div class="kicker" style="margin-top:22px">BUY 2, GET 1 FREE</div>
  <div class="head">ON CHICKEN FEED</div>
  <div class="txt">Lorem Ipsum is simply dummy text of the<br>printing and typesetting industry</div>
  <a class="btn">Shop Now</a>
  <div class="photo" role="img" aria-label="Colourful pet food pouches" style="left:38px;top:155px;width:228px;height:94px;background:linear-gradient(90deg,#f4c93a,#4ca58a 55%,#d9534b)"></div>
</div>
<div class="abs offer" style="left:444px;background:#f1e4d6">
  <div class="kicker" style="margin-top:20px;font-size:18px">SAVE 15% ON</div>
  <div class="head">PREMIUM FISH FOOD</div>
  <div class="txt">Lorem Ipsum is simply dummy text of the<br>printing and typesetting industry</div>
  <a class="btn">Shop Now</a>
  <div class="photo" role="img" aria-label="Scattered fish food pellets" style="left:0;top:150px;width:303px;height:99px;border-radius:0;background:linear-gradient(180deg,rgba(176,92,40,0),#a95a26 60%,#8a4418)"></div>
</div>
<div class="abs offer" style="left:760px">
  <div style="position:absolute;left:22px;top:35px;font-size:19px;font-weight:700;line-height:1.15">FREE<br>SHIPPING<br><span style="color:var(--orange)">OVER €50</span></div>
  <div style="position:absolute;left:22px;top:112px;width:115px;font-size:10px;line-height:1.45;color:var(--muted)">Lorem Ipsum is simply dummy text of the printing and typesetting industry</div>
  <a class="btn" style="position:absolute;left:22px;top:186px;margin:0">Shop Now</a>
  <div class="photo" role="img" aria-label="Labrador dog sitting beside a paper food bag" style="left:150px;top:20px;width:150px;height:222px;background:linear-gradient(170deg,#f3e6d2,#d8b48a)"></div>
</div>

<div class="abs trust">
  <div class="item"><svg width="38" height="26" viewBox="0 0 38 26" fill="none" stroke="#f7a441" stroke-width="1.6"><rect x="1" y="3" width="22" height="16" rx="1"/><path d="M23 8h8l5 6v5H23"/><circle cx="8" cy="21" r="3"/><circle cx="29" cy="21" r="3"/></svg><span>Free Shipping on<br>orders over €50</span></div>
  <div class="item"><svg width="30" height="34" viewBox="0 0 30 34" fill="none" stroke="#f7a441" stroke-width="1.8"><path d="M15 2l12 5v9c0 8-5 13-12 16C8 29 3 24 3 16V7z"/><path d="M9 17l4 4 8-8"/></svg><span>Trusted by Farmers<br>and Aquarists</span></div>
  <div class="item"><svg width="34" height="34" viewBox="0 0 34 34" fill="none" stroke="#f7a441" stroke-width="1.8"><path d="M30 17A13 13 0 1 1 17 4"/><path d="M17 10v8l5 3"/><path d="M22 4h6v6" stroke-dasharray="2 2"/></svg><span>Fast Delivery within<br>2–3 days</span></div>
</div>

<div class="abs usp" style="left:140px;width:180px">
  <svg width="56" height="44" viewBox="0 0 56 44" fill="none" stroke="#f7a441" stroke-width="2.2"><rect x="8" y="6" width="28" height="24" rx="2"/><path d="M36 14h10l7 8v8H36"/><circle cx="16" cy="34" r="4"/><circle cx="44" cy="34" r="4"/><path d="M15 18l5 5 9-9"/><path d="M1 12h5M1 18h5M1 24h5"/></svg>
  <h3>Fast Delivery</h3><p>Sed ut perspiciatis unde omnis iste natus error sit voluptatem accus antium doloremque laudan.</p>
</div>
<div class="abs usp-sep" style="left:342px"></div>
<div class="abs usp" style="left:372px;width:200px">
  <svg width="56" height="44" viewBox="0 0 56 44" fill="none" stroke="#f7a441" stroke-width="2.2"><path d="M6 24h36c0 9-8 15-18 15S6 33 6 24z"/><path d="M42 28h12"/><circle cx="18" cy="14" r="5"/><circle cx="30" cy="12" r="4"/><path d="M24 3v6"/></svg>
  <h3>High-Quality Ingredients</h3><p>Sed ut perspiciatis unde omnis iste natus error sit voluptatem accus antium doloremque laudan.</p>
</div>
<div class="abs usp-sep" style="left:612px"></div>
<div class="abs usp" style="left:640px;width:200px">
  <svg width="56" height="44" viewBox="0 0 56 46" fill="none" stroke="#f7a441" stroke-width="2.2"><circle cx="28" cy="11" r="7"/><path d="M18 12a10 10 0 0 1 20 0"/><rect x="12" y="26" width="32" height="16" rx="2"/><circle cx="28" cy="34" r="2"/><path d="M6 44h44"/></svg>
  <h3>Expert Support</h3><p>Sed ut perspiciatis unde omnis iste natus error sit voluptatem accus antium doloremque laudan.</p>
</div>
<div class="abs usp-sep" style="left:858px"></div>
<div class="abs usp" style="left:884px;width:200px">
  <svg width="56" height="44" viewBox="0 0 56 44" fill="none" stroke="#f7a441" stroke-width="2.2"><rect x="6" y="6" width="40" height="28" rx="2"/><path d="M6 14h40M12 22h14M12 28h8"/><path d="M42 20l8 3v6c0 5-4 8-8 10-4-2-8-5-8-10v-6z"/><path d="M39 29l2 2 4-4"/></svg>
  <h3>Secure Payment</h3><p>Sed ut perspiciatis unde omnis iste natus error sit voluptatem accus antium doloremque laudan.</p>
</div>

<h2 class="abs section-title" style="top:1746px">RECENT BLOG</h2>
<article class="abs blog" style="left:130px"><div class="photo" role="img" aria-label="Bowl of kibble with a bone treat on wood" style="background:linear-gradient(150deg,#6b4a33,#a06a3e 50%,#4a3223)"></div><h4>Lorem ipsum dolor sit amet, consectetur adipiscing elit,</h4><p>Sed ut perspiciatis unde omnis iste natus error sit voluptatem accusantium doloremque laudantium, totam rem aperiam, eaque ipsa quae.</p><a class="btn">Read More</a></article>
<article class="abs blog" style="left:367px"><div class="photo" role="img" aria-label="Dog eating from a green bowl" style="background:linear-gradient(150deg,#cfcac2,#c08a4e 60%,#b7c13a)"></div><h4>Lorem ipsum dolor sit amet, consectetur adipiscing elit,</h4><p>Sed ut perspiciatis unde omnis iste natus error sit voluptatem accusantium doloremque laudantium, totam rem aperiam, eaque ipsa quae.</p><a class="btn">Read More</a></article>
<article class="abs blog" style="left:606px"><div class="photo" role="img" aria-label="Hand feeding fish in an aquarium" style="background:linear-gradient(180deg,#9aa7ad,#2f6e78 50%,#1f4d55)"></div><h4>Lorem ipsum dolor sit amet, consectetur adipiscing elit,</h4><p>Sed ut perspiciatis unde omnis iste natus error sit voluptatem accusantium doloremque laudantium, totam rem aperiam, eaque ipsa quae.</p><a class="btn">Read More</a></article>
<article class="abs blog" style="left:845px"><div class="photo" role="img" aria-label="Cat beside a wicker basket of toy balls" style="background:linear-gradient(150deg,#e9e4dc,#a58462 50%,#e86a4a)"></div><h4>Lorem ipsum dolor sit amet, consectetur adipiscing elit,</h4><p>Sed ut perspiciatis unde omnis iste natus error sit voluptatem accusantium doloremque laudantium, totam rem aperiam, eaque ipsa quae.</p><a class="btn">Read More</a></article>

<h2 class="abs section-title" style="top:2154px">FAQ</h2>
<ul class="abs faq">
  <li>What types of products does Brenvik offer?<svg width="12" height="12" viewBox="0 0 12 12" fill="none" stroke="#1f1f1f" stroke-width="1.6"><path d="M2 10L10 2M4 2h6v6"/></svg></li>
  <li>Are your feeds suitable for all fish and chicken breeds?<svg width="12" height="12" viewBox="0 0 12 12" fill="none" stroke="#1f1f1f" stroke-width="1.6"><path d="M2 10L10 2M4 2h6v6"/></svg></li>
  <li>How can I place an order?<svg width="12" height="12" viewBox="0 0 12 12" fill="none" stroke="#1f1f1f" stroke-width="1.6"><path d="M2 10L10 2M4 2h6v6"/></svg></li>
  <li>What are your delivery times?<svg width="12" height="12" viewBox="0 0 12 12" fill="none" stroke="#1f1f1f" stroke-width="1.6"><path d="M2 10L10 2M4 2h6v6"/></svg></li>
  <li>Do you offer free shipping?<svg width="12" height="12" viewBox="0 0 12 12" fill="none" stroke="#1f1f1f" stroke-width="1.6"><path d="M2 10L10 2M4 2h6v6"/></svg></li>
  <li>Can I return or exchange a product?<svg width="12" height="12" viewBox="0 0 12 12" fill="none" stroke="#1f1f1f" stroke-width="1.6"><path d="M2 10L10 2M4 2h6v6"/></svg></li>
  <li>Are your products eco-friendly or sustainably sourced?<svg width="12" height="12" viewBox="0 0 12 12" fill="none" stroke="#1f1f1f" stroke-width="1.6"><path d="M2 10L10 2M4 2h6v6"/></svg></li>
  <li>How can I contact customer support?<svg width="12" height="12" viewBox="0 0 12 12" fill="none" stroke="#1f1f1f" stroke-width="1.6"><path d="M2 10L10 2M4 2h6v6"/></svg></li>
</ul>

<footer class="abs footer">
  <div class="abs wordmark footer-logo">Brenvik</div>
  <div class="abs col" style="left:395px">
    <h5>CONTACT US</h5>
    <div class="contact-row"><svg width="11" height="14" viewBox="0 0 11 14" fill="#fff"><path d="M5.5 0A5.5 5.5 0 0 0 0 5.5C0 9.5 5.5 14 5.5 14S11 9.5 11 5.5A5.5 5.5 0 0 0 5.5 0zm0 7.5a2 2 0 1 1 0-4 2 2 0 0 1 0 4z"/></svg><span>42 Havenkade Unit 3-12<br>Harderwijk, 3841 AB</span></div>
    <div class="contact-row" style="margin-top:16px"><svg width="12" height="12" viewBox="0 0 12 12" fill="#fff"><path d="M2.5 0l2 3-1.3 1.3a7 7 0 0 0 4.5 4.5L9 7.5l3 2-1.5 2.5C5 12 0 7 0 1.5z"/></svg><span>+31 341 555 010</span></div>
    <div class="contact-row" style="margin-top:16px"><svg width="12" height="10" viewBox="0 0 12 10" fill="#fff"><path d="M0 0h12v10H0zM1 1.2v.3L6 5l5-3.5v-.3z"/></svg><span>info@brenvik.nl</span></div>
  </div>
  <div class="abs col" style="left:621px">
    <h5>MENU</h5>
    <div class="menu"><span>Fishing</span><span>Angling</span><span>Birds</span><span>Reptiles</span><span>Dogs</span><span>Farm animals</span><span>Chickens</span><span>Other Products</span><span>Rodent</span><span>Garden animals</span></div>
  </div>
  <div class="abs col" style="left:828px">
    <h5>NEWSLETTER SUBSCRIBE</h5>
    <p style="margin-top:6px">Stay informed about news and promotions by<br>subscribing to our newsletter</p>
    <div class="email"><svg width="12" height="10" viewBox="0 0 12 10" fill="#1f1f1f"><path d="M0 0h12v10H0zM1 1.2v.3L6 5l5-3.5v-.3z"/></svg>Email id</div>
    <a class="subscribe">SUBSCRIBE</a>
  </div>
  <div class="abs rule"></div>
  <div class="abs follow">FOLLOW US<div class="social" aria-label="Social media links"><span></span><span></span><span></span><span></span><span></span></div></div>
  <div class="abs copy">Copyright © 2025 All Rights Reserved</div>
</footer>

</body>
</html>
```